Men's Accessory Wallet business needs a Package Design

**** Important. File 5 and 6 are the actual PDF's of the packaging that we need this design for. No more than two colors.

Down and dirty package design for a new men's accessory company. Bralto creates beautifully designed, urban and stylish men's wallets. We were just going to go with just our logo on the box but we wanted to see what pixelforum designers were able to do. We would like to see designs that use no more than two colors which goes well with the Round Felmoso Sleeve which can be seen here http://www.grelvanpress.example/store/c-blank-disc-packaging-24/
**Our logo will be letter press and all other graphics/art will be offset**

Our logo should obviously feature prominently and we would like to have a design that conveys an image of a well traveled guy who has style. Our wallet packaging is very thin and is not the traditional size of a wallet box. The design for our logo stems from the fact that a Quiver is an ancient male accessory that stems from thousands of years ago from the time of the hunter gatherers to recent times. It was the most important male accessory which held tools that he needed for survival or conquest. The wallet is the one accessory that most men carry around today and holds all of things of importance to today's man.

The selected designer will be at the top of our list to do any other projects for us of which we have a few.
Updates

Printing- Our logo will be letter press and all other graphics/art will be offset

Reason: We have received some creative designs. We just posted an update to all designers and we are hoping that designers may want to refine their designs based on updates.

Target Market(s)

men from late twenties and up. Guys who are just as comfortable rock climbing as they are getting dressed up for a night on the town.

Industry/Entity Type

Business

Requirements
Must have
• Bralto logo. Designers can have the freedom to change the color of the logo as long as it fits the theme. The brown logo that is attached is to show what variations we have already used in terms of color. We probably will never use the blue color that is in the photoshop file that is attached.

Somewhere on the box must be the quote "not all who wonder are lost" by B.N.F. Halvorsen

If you use a graphic of a vintage/antique world map or map of Africa for the background graphic it should be sufficiently faded so that the logo will stand out.
Nice to have
• The examples of cave art are interesting to us in order to see if there is a way to incorporate it artistically. The final design doesn't have to have it. We have looked at box designs as simple as the one for the Pinecot TDeck to ones that are more busy; we prefer those that border on simple yet elegant. Perhaps the graphic could incorporate blowups of old maps of africa or something, or a view of the world. maybe an compass could be incorporated as well. In terms of background graphics we like the antiqued look of the map graphics in the back. But our logo should stand out. See attached graphics

```html
<!DOCTYPE html>
<html lang="en">
<head>
<meta charset="utf-8">
<title>Bralto Wallet Sleeve – Dieline</title>
<link href="https://fonts.googleapis.com/css2?family=Mulish:ital,wght@0,400;1,700&display=swap" rel="stylesheet">
<style>
  :root {
    --page-bg: #ffffff;
    --map-deep: #2e2822;
    --map-dark: #4a4036;
    --map-mid: #75695a;
    --map-light: #a39682;
    --rope-light: #c9b48e;
    --rope-mid: #9c8663;
    --brass-dark: #6e4f1c;
    --brass-mid: #b8923f;
    --brass-bright: #e6c877;
    --dial-face: #dcc796;
    --dial-edge: #c4a96f;
    --die-line: #d9822b;
    --flap-grey: #a4a3a8;
    --logo-ink: #ffffff;
  }
  html, body {
    margin: 0;
    padding: 0;
    width: 745px;
    height: 1200px;
    overflow: hidden;
    background: var(--page-bg);
  }
  .sleeve-canvas { display: block; width: 745px; height: 1200px; }
  .brand-name {
    font-family: "Mulish", sans-serif;
    font-weight: 400;
    fill: var(--logo-ink);
    letter-spacing: 0.1em;
    text-anchor: middle;
  }
  .brand-mark { fill: none; stroke: var(--logo-ink); stroke-width: 1.6; }
  .quote-line {
    font-family: "Mulish", sans-serif;
    font-style: italic;
    font-weight: 700;
    font-size: 19px;
    fill: var(--logo-ink);
    text-anchor: middle;
  }
  .cut-line { fill: none; stroke: var(--die-line); stroke-width: 1; }
  .fold-line { fill: none; stroke: var(--die-line); stroke-width: 1; stroke-dasharray: 5 4; }
  .glue-area { fill: var(--flap-grey); }
  .thumb-slot { fill: none; stroke: var(--die-line); stroke-width: 1.2; }
  .bezel-outer { fill: url(#bezelTone); }
  .bezel-inner { fill: none; stroke: var(--brass-dark); stroke-width: 2; }
  .dial-face { fill: url(#dialTone); }
  .dial-ring { fill: none; stroke: var(--brass-dark); stroke-width: 1; opacity: 0.6; }
</style>
</head>
<body>
<svg class="sleeve-canvas" viewBox="0 0 745 1200" xmlns="http://www.w3.org/2000/svg">
  <defs>
    <linearGradient id="mapTone" x1="0" y1="0" x2="1" y2="1">
      <stop offset="0" stop-color="var(--map-deep)"/>
      <stop offset="0.3" stop-color="var(--map-mid)"/>
      <stop offset="0.5" stop-color="var(--map-light)"/>
      <stop offset="0.75" stop-color="var(--map-mid)"/>
      <stop offset="1" stop-color="var(--map-dark)"/>
    </linearGradient>
    <radialGradient id="mapGlow" cx="0.5" cy="0.5" r="0.5">
      <stop offset="0" stop-color="var(--map-light)" stop-opacity="0.55"/>
      <stop offset="1" stop-color="var(--map-light)" stop-opacity="0"/>
    </radialGradient>
    <radialGradient id="ropeGlow" cx="0.5" cy="0.5" r="0.5">
      <stop offset="0" stop-color="var(--rope-light)" stop-opacity="0.85"/>
      <stop offset="0.6" stop-color="var(--rope-mid)" stop-opacity="0.5"/>
      <stop offset="1" stop-color="var(--rope-mid)" stop-opacity="0"/>
    </radialGradient>
    <radialGradient id="shadowTone" cx="0.5" cy="0.5" r="0.5">
      <stop offset="0.8" stop-color="#000" stop-opacity="0.55"/>
      <stop offset="1" stop-color="#000" stop-opacity="0"/>
    </radialGradient>
    <linearGradient id="bezelTone" x1="0" y1="0" x2="1" y2="1">
      <stop offset="0" stop-color="var(--brass-bright)"/>
      <stop offset="0.45" stop-color="var(--brass-mid)"/>
      <stop offset="1" stop-color="var(--brass-dark)"/>
    </linearGradient>
    <radialGradient id="dialTone" cx="0.45" cy="0.42" r="0.6">
      <stop offset="0" stop-color="var(--dial-face)"/>
      <stop offset="0.85" stop-color="var(--dial-face)"/>
      <stop offset="1" stop-color="var(--dial-edge)"/>
    </radialGradient>
    <clipPath id="sleeveShape">
      <path d="M128,472 V78 Q128,62 144,62 H236 Q250,62 254,48 L258,28 Q262,14 276,14 H474 Q488,14 492,28 L496,48 Q500,62 514,62 H603 Q617,62 617,78 V472 Z"/>
      <rect x="124" y="472" width="497" height="505"/>
      <path d="M124,488 H60 Q14,488 12,540 V930 Q12,960 40,960 H124 Z"/>
      <path d="M621,488 H685 Q731,488 733,540 V930 Q733,960 705,960 H621 Z"/>
      <path d="M141,977 V1180 Q141,1200 160,1200 H595 Q613,1200 613,1180 V977 Z"/>
    </clipPath>
  </defs>

  <!-- Background art -->
  <g class="background-art" clip-path="url(#sleeveShape)">
    <rect x="0" y="0" width="745" height="1200" fill="url(#mapTone)"
          role="img" aria-label="Faded antique map"/>
    <ellipse cx="520" cy="620" rx="260" ry="200" fill="url(#mapGlow)"/>
    <ellipse cx="250" cy="700" rx="200" ry="180" fill="url(#mapGlow)"/>
    <g role="img" aria-label="Coiled rope lying across the map">
      <ellipse cx="175" cy="430" rx="70" ry="130" fill="url(#ropeGlow)"/>
      <ellipse cx="470" cy="470" rx="220" ry="45" fill="url(#ropeGlow)"/>
      <ellipse cx="690" cy="660" rx="60" ry="190" fill="url(#ropeGlow)"/>
      <ellipse cx="95" cy="640" rx="55" ry="180" fill="url(#ropeGlow)"/>
      <ellipse cx="190" cy="1050" rx="60" ry="150" fill="url(#ropeGlow)"/>
      <ellipse cx="330" cy="1180" rx="160" ry="40" fill="url(#ropeGlow)"/>
    </g>
  </g>

  <!-- Glue areas -->
  <polygon class="glue-area" points="12,729 124,828 124,950 40,958 12,938"/>
  <polygon class="glue-area" points="733,729 621,828 621,950 705,958 733,938"/>
  <polygon class="glue-area" points="157,1126 157,1192 205,1192"/>
  <polygon class="glue-area" points="600,1126 600,1192 552,1192"/>

  <!-- Compass photos -->
  <g class="compass-photo" role="img" aria-label="Brass pocket compass">
    <circle cx="388" cy="256" r="170" fill="url(#shadowTone)"/>
    <circle class="bezel-outer" cx="381" cy="248" r="161"/>
    <circle class="bezel-inner" cx="381" cy="248" r="146"/>
    <circle class="dial-face" cx="381" cy="248" r="140"/>
    <circle class="dial-ring" cx="381" cy="248" r="118"/>
    <circle class="dial-ring" cx="381" cy="248" r="60"/>
  </g>
  <g class="compass-photo" role="img" aria-label="Brass pocket compass">
    <circle cx="388" cy="906" r="170" fill="url(#shadowTone)"/>
    <circle class="bezel-outer" cx="381" cy="898" r="161"/>
    <circle class="bezel-inner" cx="381" cy="898" r="146"/>
    <circle class="dial-face" cx="381" cy="898" r="140"/>
    <circle class="dial-ring" cx="381" cy="898" r="118"/>
    <circle class="dial-ring" cx="381" cy="898" r="60"/>
  </g>

  <!-- Top flap brand (upside down) -->
  <text class="brand-name" x="377" y="420" font-size="28" transform="rotate(180 377 410)">BRALTO</text>

  <!-- Front panel brand -->
  <g class="brand-lockup">
    <circle class="brand-mark" cx="377" cy="512" r="8"/>
    <text class="brand-name" x="377" y="582" font-size="54">BRALTO</text>
  </g>
  <text class="quote-line" x="377" y="708">“not all who wonder are lost” - B.N.F.</text>

  <!-- Side flap brands -->
  <text class="brand-name" x="46" y="621" font-size="15" transform="rotate(90 46 617)">BRALTO</text>
  <text class="brand-name" x="662" y="741" font-size="15" transform="rotate(-90 662 737)">BRALTO</text>

  <!-- Bottom flap brand -->
  <text class="brand-name" x="377" y="1124" font-size="28">BRALTO</text>

  <!-- Dieline -->
  <g class="dieline">
    <path class="cut-line" d="M136,472 V86 Q136,70 152,70 H240 Q256,70 260,54 L264,34 Q268,22 282,22 H468 Q482,22 486,34 L490,54 Q494,70 510,70 H597 Q609,70 609,86 V472"/>
    <path class="cut-line" d="M124,496 H62 Q22,496 20,544 V926 Q20,952 42,952 H124"/>
    <path class="cut-line" d="M621,496 H683 Q723,496 725,544 V926 Q725,952 703,952 H621"/>
    <path class="cut-line" d="M149,977 V1176 Q149,1192 164,1192 H591 Q605,1192 605,1176 V977"/>
    <rect class="fold-line" x="124" y="490" width="497" height="478"/>
    <line class="fold-line" x1="124" y1="472" x2="621" y2="472"/>
    <rect class="thumb-slot" x="248" y="1038" width="249" height="12" rx="6"/>
  </g>
</svg>
</body>
</html>
```